Dietetic office: Bright Meal

I want to give my business card a modern and warm look (which attracts the eye and has a reassuring side), which links dietetics to a moment of well-being. The front and back sides must be used (not just to put the logo on the front side)

The map should be eye-catching and easy to read. I don't necessarily want to have a plain background, which I find visually weighs down the maps.
I really like the square format of a business card with rounded edges which is different from what we are used to finding (and why not take this square diagonally?), however I am not closed to another format as long as I like the style.

Who am I? Coraline, 32 years old, Dietician and passionate about food since always. I am specialized in slimming and an expert in micro nutrition, which means that I take into account not only the nutritional balance while maintaining pleasure (if foods are present in the business card, I do not want some cliché things where there would just be fruits and vegetables, but really something more global), but also the psycho-emotional dimension that I will treat with food supplements based on plants, fruits or vegetables.

-----------------------------------------------------------------------------------

 Mention to appear on the card IN FRENCH (please be careful in case of translation that the use of words is correct):

Coraline MAUREL
Dietician Nutritionist
Expert in Slimming and Micro-Nutrition

Slogan: I help you lose weight sustainably with pleasure and by reconciling your events

Catchphrases: Want to lose weight? Do you like going out? Do you have a lot of events? And is pleasure on your plate important to you?

Make an appointment on Rendivo or on 06 41 83 52 17
coraline.brightmeal@exemplonet.fr
Address: Health Center, Allée des Glycines, 13492 Vitrolles
www.brightmeal-exemple.fr
Chatterbook + Picturegram Logo

- The company logo has been uploaded for your viewing. Other file formats can be made available if required.
- I would like a place for a photo of me to be possible.
Updates

Good morning,
I want to have a business card that is both lively and warm. Which will easily catch the eye while being easy to read and make people understand that I am in the field of well-being.
I like the square side in business cards (and why not use them diagonally?), or a more classic but original one.
Both the front and back sides must be used (I don't want to have the logo on just one side)
I don't want to have a plain background, but rather something more muted (I really like the suggestion from "Pine Kettle Graphic Designer" for this)
the use of logo for telephone, mail, address, rendivo, chatterbook, picto etc is possible in order to facilitate reading

Please follow the various elements of the brief regarding the text and use the French text as it is.

I like business cards preferably square (with the possibility of using them diagonally).
The map should be eye-catching and easy to read.
It must bring pep while having softness which brings back to the well-being side
The card must be used on the front and back for the different elements (I do not want to have only the logo on the front side)
The text must correspond to the brief (be careful with the translation which can sometimes be bad)
I don't want to have a plain blue or orange background. I really like the idea of the background from "Pine Kettle Graphic Designer"

You can if you wish use symbols for contacts, telephone, rendivo, address, cb, picto....

Target Market(s)

mainly women between 25 and 65 years old + men around 40 years old

Contact Information for Business Card

22

Font styles to use
Sans Serif
Script

Colors
0054AA
0677BA
7BADD7
CADEEF
E8F1F8
0094D4
00A9DD
6FCCEA
C7EBF8
E9F6FB
00AB8E
00BBA5
67D7C9
C6EFE9
E9F9F6
FFC000
F8CF3A
FAE287
FDF2CF
FEFAEE
F0912C
F2A743
F7CA91
FBE8D2
FDF5EE

Requirements
Must have
• some pep! while being refined
Nice to have
• I really like the square format of a business card with rounded edges which is different from what we are used to finding, however I am not closed to another format as long as I like the style.
Should not have
• if foods are represented, only show fruits and vegetables (too cliché)

```html
<!DOCTYPE html>
<html lang="fr">
<head>
<meta charset="utf-8">
<title>Bright Meal – carte de visite</title>
<link href="https://fonts.googleapis.com/css2?family=Dancing+Script:wght@500;600&family=Open+Sans:ital,wght@0,400;0,600;0,700;1,400&display=swap" rel="stylesheet">
<style>
  :root {
    --stage: #4a4a4a;
    --card: #ffffff;
    --blue-deep: #0054AA;
    --blue: #0677BA;
    --blue-bright: #0094D4;
    --blue-band: #1f8fe0;
    --cyan: #3fd0e6;
    --blue-soft: #7BADD7;
    --orange: #F0912C;
    --orange-soft: #F2A743;
    --orange-band: #f6b24e;
    --green: #00BBA5;
  }
  * { box-sizing: border-box; margin: 0; padding: 0; }
  html, body { width: 1200px; height: 597px; overflow: hidden; }
  body {
    background: var(--stage);
    font-family: "Open Sans", sans-serif;
    position: relative;
  }
  .card {
    position: absolute;
    top: 23px;
    width: 548px;
    height: 549px;
    border-radius: 24px;
    overflow: hidden;
    background: var(--card);
  }
  .card--front { left: 23px; }
  .card--back { left: 620px; }
  .card__backdrop {
    position: absolute; inset: 0;
    background:
      radial-gradient(circle at 10% 22%, rgba(247,150,90,.28), transparent 30%),
      radial-gradient(circle at 88% 85%, rgba(240,145,44,.22), transparent 32%),
      radial-gradient(circle at 60% 60%, rgba(110,190,120,.16), transparent 40%),
      linear-gradient(160deg, #fbf8f4, #f3f1ee);
  }
  .card__veil {
    position: absolute; inset: 0;
    background: rgba(255,255,255,.72);
  }
  .brand {
    position: absolute; left: 0; right: 0;
    text-align: center;
    color: var(--blue-bright);
  }
  .brand__name { display: block; font-weight: 400; line-height: 1; }
  .brand__tagline { display: block; color: var(--blue); margin-top: 4px; }
  .card--front .brand { top: 84px; }
  .card--front .brand__name { font-size: 46px; }
  .card--front .brand__tagline { font-size: 12px; padding-left: 150px; }
  .card--back .brand { top: 62px; }
  .card--back .brand__name { font-size: 28px; }
  .card--back .brand__tagline { font-size: 8px; padding-left: 90px; margin-top: 1px; }

  .band {
    position: absolute;
    color: #fff;
    font-size: 24px;
    display: flex; align-items: center;
  }
  .band--blue {
    left: 0; top: 204px; width: 354px; height: 54px;
    background: var(--blue-band);
    border-radius: 0 14px 14px 0;
    transform: skewY(-1.5deg);
    padding-left: 57px;
  }
  .band--cyan {
    left: 193px; top: 276px; width: 360px; height: 53px;
    background: var(--cyan);
    border-radius: 14px 0 0 14px;
    transform: skewY(-1.5deg);
    padding-left: 42px;
  }
  .band--orange {
    left: 30px; top: 353px; width: 486px; height: 53px;
    background: var(--orange-band);
    border-radius: 27px;
    justify-content: center;
    font-size: 22px;
  }
  .front__question {
    position: absolute; left: 0; right: 0; top: 444px;
    text-align: center;
    color: var(--blue-bright);
    font-size: 23px; font-weight: 700;
    line-height: 37px;
  }

  .profile {
    position: absolute;
    left: 33px; top: 126px; width: 481px; height: 294px;
    border: 2px solid var(--blue-soft);
    border-radius: 22px;
    background: rgba(255,255,255,.93);
  }
  .profile__portrait {
    position: absolute; left: 13px; top: 2px; width: 155px; height: 206px;
    border-radius: 10px;
    background: linear-gradient(180deg, #e9eef5 0%, #d9b89c 55%, #8c1c22 100%);
  }
  .profile__name {
    position: absolute; left: 170px; right: 0; top: 12px;
    text-align: center;
    font-family: "Dancing Script", cursive;
    font-size: 36px; font-weight: 500;
    color: var(--blue-bright);
  }
  .profile__role {
    position: absolute; left: 170px; right: 0; top: 60px;
    text-align: center;
    color: var(--orange-soft);
    font-size: 16px; line-height: 25px;
  }
  .profile__cta {
    position: absolute; left: 170px; right: 0; top: 118px;
    text-align: center;
    font-family: "Dancing Script", cursive;
    font-size: 25px; font-weight: 600;
    color: var(--blue-bright);
  }
  .profile__phone {
    position: absolute; left: 170px; right: 0; top: 152px;
    text-align: center;
    font-size: 26px; font-weight: 700; letter-spacing: .5px;
    color: var(--blue-bright);
  }
  .profile__online {
    position: absolute; left: 170px; right: 0; top: 192px;
    text-align: center;
    font-size: 13px; font-weight: 700;
    color: var(--orange-soft);
  }
  .profile__slogan {
    position: absolute; left: 0; right: 0; top: 220px;
    text-align: center;
    font-size: 19px; font-style: italic;
    line-height: 30px;
    color: var(--blue);
  }

  .contact {
    position: absolute; left: 39px; top: 442px;
    color: var(--blue);
  }
  .contact__email { font-size: 16px; font-weight: 700; color: var(--blue-bright); }
  .contact__address { margin-top: 20px; font-size: 15px; line-height: 22px; font-weight: 600; }
  .social {
    position: absolute; right: 40px; top: 444px;
    display: flex; flex-direction: column; align-items: flex-start; gap: 6px;
    color: var(--blue-bright);
    font-size: 13px; font-weight: 700;
  }
  .social__item { display: flex; align-items: center; gap: 6px; }
  .social__mark { width: 14px; height: 14px; border-radius: 3px; background: var(--blue-bright); }
  .contact__web {
    position: absolute; right: 40px; top: 503px;
    color: var(--blue-bright);
    font-size: 18px; font-weight: 700;
  }
</style>
</head>
<body>
  <section class="card card--front">
    <div class="card__backdrop" role="img" aria-label="Photo floue d'un plat coloré de légumes et céréales en fond"></div>
    <div class="card__veil"></div>
    <div class="brand">
      <span class="brand__name">Bright Meal</span>
      <span class="brand__tagline">La clé de votre bien être</span>
    </div>
    <div class="band band--blue">Envie de mincir ?</div>
    <div class="band band--cyan">Vous aimez sortir ?</div>
    <div class="band band--orange">Vous avez beaucoup d'évènements ?</div>
    <p class="front__question">Le plaisir dans votre assiette est<br>important pour vous ?</p>
  </section>

  <section class="card card--back">
    <div class="card__backdrop" role="img" aria-label="Photo floue d'un plat coloré de légumes en fond"></div>
    <div class="card__veil"></div>
    <div class="brand">
      <span class="brand__name">Bright Meal</span>
      <span class="brand__tagline">La clé de votre bien être</span>
    </div>
    <div class="profile">
      <div class="profile__portrait" role="img" aria-label="Portrait illustré de la diététicienne"></div>
      <h1 class="profile__name">Coraline Maurel</h1>
      <p class="profile__role">Diététicienne nutritionniste<br>Experte en amincissement</p>
      <p class="profile__cta">Prenez rendez-vous</p>
      <p class="profile__phone">06 41 83 52 17</p>
      <p class="profile__online">ou sur rendivo.fr</p>
      <p class="profile__slogan">Je vous aide à mincir durablement<br>avec plaisir, en conciliant vos évènements</p>
    </div>
    <div class="contact">
      <p class="contact__email">coraline.brightmeal@exemplonet.fr</p>
      <p class="contact__address">Espace de santé<br>allée des Glycines 13492 Vitrolles</p>
    </div>
    <div class="social">
      <span class="social__item"><span class="social__mark"></span>Chatterbook</span>
      <span class="social__item"><span class="social__mark"></span>Picturegram</span>
    </div>
    <p class="contact__web">brightmeal.fr</p>
  </section>
</body>
</html>
```